Webdesign für berufliches Schulzentrum für Ernährung, Gastgewerbe, Gesundheit
Zielgruppe
Berufliches Schulzentrum für Ernährung, Gastgewerbe, Gesundheit
Zielgruppe: Schüler und Auszubildende
Aufgabenstellung
- modernes, aber dennoch strukturiertes Aussehen der Webseite
- einfache Navigation
- die beiden Grüntöne aus dem Logo sollen sich bitte in der Seite wiederfinden - jedoch in freundlicher Form

```html
<!DOCTYPE html>
<html lang="de">
<head>
<meta charset="utf-8">
<title>Schularten – BSZ Lindenhof</title>
<link href="https://fonts.googleapis.com/css2?family=Work+Sans:wght@400;500;600&display=swap" rel="stylesheet">
<style>
  :root {
    --bg: #f2f2f2;
    --page: #ffffff;
    --ink: #1d1d1d;
    --muted: #555b57;
    --green-dark: #1e4a2c;
    --green-mid: #5f8d6d;
    --green-soft: #c9ebd4;
    --hero-a: #8fb39a;
    --hero-b: #2c5638;
  }
  * { box-sizing: border-box; margin: 0; padding: 0; }
  html, body { width: 1200px; height: 1200px; overflow: hidden; }
  body { background: var(--bg); font-family: "Work Sans", sans-serif; color: var(--ink); position: relative; }

  .board-label {
    position: absolute; left: 120px; top: 1160px;
    transform: rotate(-90deg); transform-origin: left top;
    font-size: 27px; color: var(--muted); font-weight: 400; white-space: nowrap;
  }

  .page {
    position: absolute; left: 173px; top: 35px; width: 854px; height: 1130px;
    background: var(--page); box-shadow: 0 2px 8px rgba(0,0,0,.18);
  }

  .site-header { position: absolute; left: 0; top: 0; width: 100%; height: 63px; background: #f4f4f4; }
  .brand {
    position: absolute; left: 13px; top: 18px; display: flex; align-items: center; gap: 6px;
    font-size: 12px; font-weight: 600; color: var(--green-dark); letter-spacing: .5px;
  }
  .brand-square { width: 12px; height: 12px; background: var(--green-soft); }
  .nav-item {
    position: absolute; top: 27px; font-size: 8px; font-weight: 600; letter-spacing: 1.6px;
    color: var(--ink); text-transform: uppercase;
  }
  .nav-item.active::after {
    content: ""; position: absolute; left: 0; top: 11px; width: 16px; height: 1px; background: var(--green-dark);
  }
  .menu-icon { position: absolute; left: 819px; top: 24px; }

  .hero {
    position: absolute; left: 0; top: 63px; width: 100%; height: 211px;
    background: linear-gradient(100deg, var(--hero-a) 0%, #6e967a 45%, var(--hero-b) 100%);
  }
  .hero-sub {
    position: absolute; top: 63px; width: 100%; text-align: center;
    color: #fff; font-size: 12.5px; font-weight: 500; letter-spacing: 1.2px;
  }
  .hero-title {
    position: absolute; left: 198px; top: 87px; width: 459px; height: 40px;
    background: rgba(255,255,255,.2); color: #fff; text-align: center;
    font-size: 29px; font-weight: 500; letter-spacing: 5px; line-height: 40px;
  }

  .card {
    position: absolute; top: 308px; width: 221px; height: 281px; background: #fff;
    box-shadow: 0 1px 5px rgba(0,0,0,.28); text-align: center;
  }
  .card-photo { width: 100%; height: 113px; }
  .card-title { margin-top: 12px; font-size: 13px; font-weight: 600; letter-spacing: 3.2px; }
  .card-list { list-style: none; margin-top: 10px; font-size: 11.4px; letter-spacing: 1px; color: var(--muted); line-height: 18.6px; }
  .card-list .tight { line-height: 15px; }
  .card-list .gap { margin-top: 20px; }

  .hint { position: absolute; left: 60px; top: 627px; font-size: 9.5px; letter-spacing: .7px; }
  .hint-rule { position: absolute; left: 0; top: 659px; width: 351px; height: 1px; background: var(--green-mid); }
  .cta-line {
    position: absolute; left: 650px; width: 204px; height: 20px; background: var(--green-soft);
    font-size: 11.8px; letter-spacing: 1.8px; line-height: 20px; padding-left: 6px; color: var(--ink);
  }

  .video { position: absolute; left: 82px; top: 710px; width: 698px; height: 358px; }
  .video-frame { width: 100%; height: 100%; background: linear-gradient(180deg, #b9d3e6 0%, #dfe5e2 45%, #8aa38d 100%); }
  .video-play { position: absolute; left: 350px; top: 155px; }
  .video-bar { position: absolute; left: 82px; top: 1068px; width: 698px; height: 26px; background: #c5ead3; }

  .site-footer { position: absolute; left: 0; bottom: 0; width: 100%; height: 10px; background: var(--green-dark); }
</style>
</head>
<body>
  <div class="board-label">Schularten Seite</div>

  <main class="page">
    <header class="site-header">
      <div class="brand"><span class="brand-square"></span>BSZ Lindenhof</div>
      <nav>
        <span class="nav-item" style="left:140px">Über uns</span>
        <span class="nav-item active" style="left:210px">Schularten</span>
        <span class="nav-item" style="left:296px">Pläne/Termine</span>
        <span class="nav-item" style="left:395px">Aktuelles</span>
        <span class="nav-item" style="left:472px">Schulanmeldung</span>
        <span class="nav-item" style="left:580px">Impression</span>
        <span class="nav-item" style="left:656px">Förderverein</span>
        <span class="nav-item" style="left:749px">Kontakt</span>
      </nav>
      <svg class="menu-icon" width="18" height="14" viewBox="0 0 18 14">
        <rect y="0" width="18" height="1.3" fill="#1d1d1d"/>
        <rect y="6" width="18" height="1.3" fill="#1d1d1d"/>
        <rect y="12" width="18" height="1.3" fill="#1d1d1d"/>
      </svg>
    </header>

    <section class="hero" role="img" aria-label="Hände kneten Teig auf bemehlter Arbeitsfläche, grün getönt">
      <p class="hero-sub">Berufsschule - Beruftsfachschule - Berufsvorbereitung</p>
      <h1 class="hero-title">UNSERE SCHULARTEN.</h1>
    </section>

    <article class="card" style="left:56px">
      <div class="card-photo" role="img" aria-label="Konditorin hält eine verzierte Torte" style="background:linear-gradient(90deg,#2a1e1c,#e6a7c0 30%,#efe6dc 55%,#2a2422)"></div>
      <h2 class="card-title">ERNÄHRUNG</h2>
      <ul class="card-list">
        <li>Bäcker/in</li>
        <li>Konditor/in</li>
        <li>Fachverkäufer/in Bäckerei</li>
        <li>Fachverkäufer/in Fleischerei</li>
        <li>Fachpraktiker/-in Bäckerei</li>
      </ul>
    </article>

    <article class="card" style="left:323px">
      <div class="card-photo" role="img" aria-label="Köchin würzt Salat in einer Profiküche" style="background:linear-gradient(90deg,#3a3733,#cfc8bc 50%,#4a4640)"></div>
      <h2 class="card-title">GASTGEWERBE</h2>
      <ul class="card-list">
        <li>Koch/Köchin</li>
        <li>Hotelfachmann/-frau</li>
        <li>Restaurantfachmann/-frau</li>
        <li>Fachmann/-frau für</li>
        <li>Systemgastronomie</li>
        <li>Fachkraft im Gastgewerbe</li>
      </ul>
    </article>

    <article class="card" style="left:587px">
      <div class="card-photo" role="img" aria-label="Ärztin hält die Hände einer Patientin" style="background:linear-gradient(90deg,#5a6270,#c9a99a 50%,#eef0f2)"></div>
      <h2 class="card-title">GESUNDHEIT</h2>
      <ul class="card-list">
        <li>Informationen</li>
        <li class="tight">Pharmazeutisch-technische/r</li>
        <li class="tight">Assistent/in</li>
        <li class="gap">Flyer Ausbildung PTA</li>
        <li>Flyer Schnupperkurs</li>
      </ul>
    </article>

    <p class="hint">Durch das Klicken auf den jeweiligen Ausbildungsberuf gelangen Sie zu mehr Infomaterial. (PDF)</p>
    <div class="hint-rule"></div>
    <div class="cta-line" style="top:614px">Hier geht es</div>
    <div class="cta-line" style="top:637px">zur Berufsvorbereitung.</div>

    <div class="video">
      <div class="video-frame" role="img" aria-label="Video-Standbild: Schulgebäude mit Bäumen unter blauem Himmel"></div>
      <svg class="video-play" width="36" height="42" viewBox="0 0 36 42"><polygon points="0,0 36,21 0,42" fill="rgba(255,255,255,.85)"/></svg>
    </div>
    <div class="video-bar">
      <svg width="698" height="26" viewBox="0 0 698 26">
        <polygon points="16,7 28,13 16,19" fill="#fff"/>
        <rect x="40" y="12.5" width="615" height="1.2" fill="#fff"/>
        <circle cx="198" cy="13" r="3.5" fill="#fff"/>
        <text x="670" y="15.5" font-size="6" fill="#fff" font-family="Work Sans, sans-serif">2:34</text>
      </svg>
    </div>

    <footer class="site-footer"></footer>
  </main>
</body>
</html>
```